UX Design Document Management App Project

UPDATED PROJECT and INCREASED TOTAL COST. Also added a new design guideline document (4QK - Concept - The Lantern 170613.pdf).

We are a small start-up company based in Sydney, Australia. We have the ideas and coding skills to have built a revolutionary document management app that helps knowledge workers deal with information overload.

We are about to launch an alpha version of a document management app on the iPhone. We have created a series of screens but they lack the brilliance that only a talented graphic designer can deliver. So we would like to find a design partner who can make a contribution in two areas:

1. Make specific changes to our screens such as formatting images so they better blend into the background.
2. Examine our overall UX and either suggest changes or propose new design concepts.
3. Create a logo for this product.

We have completed a pretty comprehensive design brief that we attach to this project and also a set of our existing screen designs in a mix of Photoshop and Keynote formats that we can share with you.

Once we have launched are alpha product, we hope that the winner of this project (our future graphic design partner) will work with us on another project that aims to radically improve the UX of our app in time for a full version 1.0 launch later this year.

We'd like to lock-down the alpha UX in 5 to 10 days but if the ideas you have are exciting enough we can extend this time.
Updates

Project now has a SIGNIFICANTLY INCREASED BUDGET (almost doubled) and an expanded scope to deliver a logo for our product. Check out the additional design brief document just uploaded.

Hello Designers,

Just to let you know that we have updated the project and INCREASED THE TOTAL BUDGET. We have also added a new design guideline document (4QK - Concept - The Lantern 170613.pdf) to help inspire you!

The project now has a significantly increased budget (almost doubled) and an expanded scope to also deliver a logo for our Mollant product. Check out the additional design brief document just uploaded.

Thanks for participating!

All the best,

Gareth

Barring any unforeseen circumstances, this design competition will remain open until midnight Pacific Standard Time this Sunday. That means about 10 am Sydney time this Monday, July 1st. Good luck and get your designs in!

Project Deadline Extended
Reason: I agreed to use PST not AEST!

Target Market(s)

individual knowledge workers: professionals, office workers/managers, university students, academics/researchers, etc.

Industry/Entity Type

Graphic Designer

Requirements
Must have
• professional, highly effective UX

```html
<!DOCTYPE html>
<html lang="en">
<head>
<meta charset="utf-8">
<title>Generating Result</title>
<link rel="stylesheet" href="https://fonts.googleapis.com/css2?family=Montserrat:wght@300;400;500;600;700&display=swap">
<style>
  :root {
    --white: #ffffff;
    --ink: #000000;
    --scene-light: #a39884;
    --scene-mid: #5b5750;
    --scene-dark: #222121;
    --panel: rgba(150, 150, 150, 0.28);
    --track: #dcdcdc;
    --seg-organizations: #4fadf0;
    --seg-places: #98d432;
    --seg-industries: #f7d22c;
    --seg-technologies: #f47b20;
    --seg-other: #6a6a6a;
    --seg-people: #c655f5;
    --seam: #3b3a38;
    --accent: #c655f5;
  }
  html, body {
    margin: 0;
    padding: 0;
    width: 676px;
    height: 1200px;
    overflow: hidden;
    background: var(--scene-dark);
  }
  .canvas {
    width: 676px;
    height: 1200px;
    overflow: hidden;
    position: relative;
  }
  .screen {
    position: absolute;
    top: 0;
    left: 0;
    width: 640px;
    height: 1136px;
    transform: scale(1.05625);
    transform-origin: 0 0;
    font-family: "Montserrat", sans-serif;
    color: var(--white);
  }
  .scene-backdrop {
    position: absolute;
    inset: 40px 0 0 0;
    background:
      radial-gradient(ellipse 300px 500px at 60px 300px, rgba(190, 178, 155, 0.55), transparent 70%),
      linear-gradient(115deg, var(--scene-light) 0%, var(--scene-mid) 38%, var(--scene-dark) 68%, #1a1a1a 100%);
  }
  .status-bar {
    position: absolute;
    top: 0;
    left: 0;
    width: 640px;
    height: 40px;
    background: var(--white);
  }
  .status-bar svg { display: block; }
  .result-view {
    position: absolute;
    top: 0;
    left: 0;
  }
  .progress-panel {
    position: absolute;
    left: 0;
    top: 915px;
    width: 640px;
    height: 221px;
    background: var(--panel);
  }
  .progress-label {
    position: absolute;
    left: 56px;
    top: 1017px;
    font-size: 17px;
    font-weight: 400;
    margin: 0;
  }
  .degree-count {
    position: absolute;
    right: 54px;
    top: 958px;
    font-size: 72px;
    font-weight: 500;
    color: var(--accent);
    margin: 0;
    line-height: 1;
  }
  .progress-track {
    position: absolute;
    left: 55px;
    top: 1063px;
    width: 530px;
    height: 12px;
    background: var(--track);
  }
  .progress-fill {
    width: 330px;
    height: 100%;
    background: var(--accent);
  }
  .label-value { font-size: 32px; font-weight: 300; fill: var(--white); }
  .label-name { font-size: 18px; font-weight: 400; fill: var(--white); }
  .leader { fill: none; stroke: var(--white); stroke-width: 1.5; }
  .total-value { font-size: 92px; font-weight: 700; fill: var(--white); }
  .total-name { font-size: 26px; font-weight: 400; fill: var(--white); }
  .screen-title { font-size: 20px; font-weight: 400; fill: var(--white); letter-spacing: 0.3px; }
  .seam { stroke: var(--seam); stroke-width: 1.2; }
  .status-text { font-family: "Montserrat", sans-serif; font-size: 20px; fill: var(--ink); }
</style>
</head>
<body>
<div class="canvas">
  <div class="screen">
    <div class="scene-backdrop" role="img" aria-label="Blurred photograph of a bridge structure in warm grey tones"></div>

    <header class="status-bar">
      <svg width="640" height="40" viewBox="0 0 640 40">
        <g class="signal" fill="var(--ink)" stroke="var(--ink)" stroke-width="1.2">
          <circle cx="16" cy="20" r="5"/>
          <circle cx="30" cy="20" r="5"/>
          <circle cx="44" cy="20" r="5"/>
          <circle cx="58" cy="20" r="4.4" fill="none"/>
          <circle cx="72" cy="20" r="4.4" fill="none"/>
        </g>
        <text class="status-text" x="86" y="28">VELA</text>
        <g class="wifi" fill="none" stroke="var(--ink)" stroke-width="2.6" stroke-linecap="round">
          <path d="M144 15 a14 14 0 0 1 20 0"/>
          <path d="M148 19.5 a8 8 0 0 1 12 0"/>
          <circle cx="154" cy="25" r="1.8" fill="var(--ink)" stroke="none"/>
        </g>
        <text class="status-text" x="320" y="28" text-anchor="middle" font-weight="600">4:21 PM</text>
        <path d="M484 14 l12 11 l-6 5 v-20 l6 5 l-12 11" fill="none" stroke="var(--ink)" stroke-width="1.6" stroke-linejoin="round"/>
        <text class="status-text" x="510" y="28">100%</text>
        <rect x="580" y="12" width="42" height="17" rx="3" fill="none" stroke="var(--ink)" stroke-width="1.6"/>
        <rect x="583" y="15" width="36" height="11" rx="1" fill="var(--ink)"/>
        <rect x="623" y="17" width="3" height="7" rx="1" fill="var(--ink)"/>
      </svg>
    </header>

    <svg class="result-view" width="640" height="915" viewBox="0 0 640 915">
      <text class="screen-title" x="320" y="128" text-anchor="middle">GENERATING RESULT</text>

      <g class="donut-chart">
        <circle cx="320" cy="475" r="113" fill="rgba(0,0,0,0.12)"/>
        <g fill="none" stroke-width="55">
          <circle class="segment-organizations" cx="320" cy="475" r="140.5" stroke="var(--seg-organizations)" stroke-dasharray="208.4 882.8" transform="rotate(229 320 475)"/>
          <circle class="segment-places" cx="320" cy="475" r="140.5" stroke="var(--seg-places)" stroke-dasharray="203.5 882.8" transform="rotate(-46 320 475)"/>
          <circle class="segment-industries" cx="320" cy="475" r="140.5" stroke="var(--seg-industries)" stroke-dasharray="63.8 882.8" transform="rotate(37 320 475)"/>
          <circle class="segment-technologies" cx="320" cy="475" r="140.5" stroke="var(--seg-technologies)" stroke-dasharray="218.2 882.8" transform="rotate(63 320 475)"/>
          <circle class="segment-other" cx="320" cy="475" r="140.5" stroke="var(--seg-other)" stroke-dasharray="68.7 882.8" transform="rotate(152 320 475)"/>
          <circle class="segment-people" cx="320" cy="475" r="140.5" stroke="var(--seg-people)" stroke-dasharray="120.2 882.8" transform="rotate(180 320 475)"/>
        </g>
        <g class="seams">
          <line class="seam" x1="398.5" y1="393.7" x2="436.8" y2="354.2"/>
          <line class="seam" x1="410.3" y1="543.0" x2="454.2" y2="576.1"/>
          <line class="seam" x1="371.3" y1="575.7" x2="396.3" y2="624.7"/>
          <line class="seam" x1="220.2" y1="528.0" x2="171.7" y2="553.8"/>
          <line class="seam" x1="207" y1="475" x2="152" y2="475"/>
          <line class="seam" x1="245.9" y1="389.7" x2="209.8" y2="348.2"/>
        </g>
        <text class="total-value" x="320" y="478" text-anchor="middle">34</text>
        <text class="total-name" x="320" y="512" text-anchor="middle">Bridges</text>
      </g>

      <g class="chart-label label-organizations">
        <polyline class="leader" points="320,290 350,240 498,240"/>
        <text class="label-value" x="498" y="227" text-anchor="end">18</text>
        <text class="label-name" x="498" y="265" text-anchor="end">Organizations</text>
      </g>
      <g class="chart-label label-people">
        <polyline class="leader" points="158,390 128,362 44,362"/>
        <text class="label-value" x="43" y="351">16</text>
        <text class="label-name" x="44" y="388">People</text>
      </g>
      <g class="chart-label label-places">
        <polyline class="leader" points="498,458 522,432 603,432"/>
        <text class="label-value" x="603" y="420" text-anchor="end">20</text>
        <text class="label-name" x="603" y="458" text-anchor="end">Places</text>
      </g>
      <g class="chart-label label-other">
        <polyline class="leader" points="156,518 128,546 52,546"/>
        <text class="label-value" x="51" y="535">6</text>
        <text class="label-name" x="52" y="570">Other</text>
      </g>
      <g class="chart-label label-industries">
        <polyline class="leader" points="432,607 474,650 598,650"/>
        <text class="label-value" x="598" y="636" text-anchor="end">6</text>
        <text class="label-name" x="598" y="677" text-anchor="end">Industries</text>
      </g>
      <g class="chart-label label-technologies">
        <polyline class="leader" points="258,635 192,700 58,700"/>
        <text class="label-value" x="57" y="688">26</text>
        <text class="label-name" x="58" y="727">Technologies</text>
      </g>
    </svg>

    <section class="progress-panel"></section>
    <p class="progress-label">Linking open data...</p>
    <p class="degree-count">4°</p>
    <div class="progress-track"><div class="progress-fill"></div></div>
  </div>
</div>
</body>
</html>
```